Flyer-Design für Wandschränke
Zielgruppe
Wir haben ein Profil entwickelt, welches es ermöglicht Schränke flächenbündig in Wände einzubauen. Das Profil ist aus MDF (Mitteldichte Holzfaserplatte) hergestellt und wird mit einer speziellen Fräsung versehen. Dieses Profil wird dann am Schrank befestigt und dient der Aufnahme der Gipskartonplatte. Der Name lautet RAHMO 3.1 Entwurf Jörg Wendtner. Das profil selbst ist zum Patent angemeldet. Unsere Zielgruppe sind Möbelhäuser und Küchenstudios.
Aufgabenstellung
Im Flyer sollte die Konstruktion und das fertige Produkt erkenbar sein. Der Flyer könnte DIN A4 sein, muss aber nicht!

```html
<!DOCTYPE html>
<html lang="de">
<head>
<meta charset="utf-8">
<title>RAHMO 3.1 – Lüftung als Designelement</title>
<link href="https://fonts.googleapis.com/css2?family=Jost:wght@300;400&display=swap" rel="stylesheet">
<style>
  :root {
    --stage: #e7e3dd;
    --paper: #f4f4f3;
    --paper-shade: #e2e2e2;
    --ink: #2f2f2f;
    --ink-soft: #555555;
    --accent: #e6dc4e;
    --frame: #f2f2f2;
    --shadow: rgba(0,0,0,.18);
  }
  * { box-sizing: border-box; margin: 0; padding: 0; }
  html, body { width: 1200px; height: 900px; overflow: hidden; }
  body { background: var(--stage); font-family: "Jost", sans-serif; color: var(--ink); position: relative; }

  .spread { position: absolute; left: 40px; width: 1120px; height: 395px; display: flex; box-shadow: 0 4px 14px var(--shadow); }
  .spread--inside { top: 35px; }
  .spread--outside { top: 465px; height: 400px; }
  .panel { position: relative; height: 100%; overflow: hidden; }

  /* inside: text panel */
  .panel--text { width: 351px; background: var(--paper); padding: 24px 39px 0 27px; }
  .section-title { font-weight: 400; font-size: 17px; letter-spacing: .4px; text-transform: uppercase; color: var(--ink); }
  .section-title--second { margin-top: 40px; text-transform: none; }
  .body-copy { margin-top: 12px; font-weight: 300; font-size: 11.6px; line-height: 16px; text-align: justify; hyphens: auto; color: var(--ink-soft); }

  .photo { position: absolute; }
  .panel--construction { width: 208px; }
  .panel--construction .photo { inset: 0; background: linear-gradient(100deg, #2b2b2b 0%, #4a4744 45%, #c9b89a 70%, #3a3a3a 100%); }

  .panel--kitchen { width: 561px; }
  .panel--kitchen .photo--room { inset: 0; background: linear-gradient(180deg, #6d6a67 0%, #b9b6b2 38%, #e4e3e1 62%, #8f8d8b 100%); }
  .panel--kitchen .photo--detail { left: 405px; top: 225px; width: 156px; height: 170px; background: linear-gradient(180deg, #e6e6e6 0 22%, #3d4048 22% 100%); }

  .brand { position: absolute; display: flex; align-items: center; gap: 10px; background: #fff; padding: 8px 12px; }
  .brand__mark { width: 34px; height: 34px; background: var(--accent); flex: none; }
  .brand__name { font-weight: 400; font-size: 15px; line-height: 18px; color: var(--ink); letter-spacing: .3px; }
  .panel--kitchen .brand { left: 12px; top: 15px; }

  .frame-lines { position: absolute; inset: 0; width: 100%; height: 100%; }

  /* outside */
  .panel--back-photo { width: 199px; }
  .panel--back-photo .photo { inset: 0; background: linear-gradient(90deg, #2a2928 0%, #d9d6d1 30%, #b9b3ab 55%, #7a5a40 70%, #2b2725 100%); }
  .panel--back { width: 360px; background: linear-gradient(90deg, var(--paper) 0%, #fafafa 100%); border-right: 1px solid var(--paper-shade); }
  .address { position: absolute; left: 41px; bottom: 14px; font-style: normal; font-weight: 300; font-size: 12.4px; line-height: 16.2px; color: var(--ink-soft); }

  .panel--cover { width: 561px; background: linear-gradient(90deg, #f2f2f2 0%, #dedede 100%); }
  .panel--cover .section-title { position: absolute; right: 10px; top: 62px; font-size: 18px; }
  .panel--cover .photo--portrait { left: 272px; top: 89px; width: 289px; height: 202px; background: linear-gradient(180deg, #bdbdbd 0%, #8a8a8a 45%, #3f3f3f 100%); }
  .panel--cover .brand { left: 150px; top: 248px; }
</style>
</head>
<body>

<section class="spread spread--inside">
  <div class="panel panel--text">
    <h2 class="section-title">Lüftung als Designelement</h2>
    <p class="body-copy">Man sieht sie oft, gerade im Premiumbereich: Flächenbündig in die Wand eingelassene Küchenschränke und Geräte. Beim Endverbraucher zu Hause schauen die Lösungen leider oftmals nicht mehr so schick aus wie auf Fotos oder in Ausstellungen. Weil es in der Praxis Lüftungsgitter über oder unter den Geräten braucht. Jörg Wendtner war das schon länger ein Dorn im Auge. Aktiv wurde er, als ein guter Freund eine Küche kaufen wollte, „wie man sie in Prospekten sieht“ – eben in die Wand eingelassen, aber ohne Lüftungsgitter.</p>
    <h2 class="section-title section-title--second">RAHMO 3.1</h2>
    <p class="body-copy">Wendtner begann zu tüfteln. Als gelernter Tischler kannte er sich mit Holzwerkstoffen aus; durch eine frühere Tätigkeit als Trockenbauer war ihm Rigips als Material vertraut. Er experimentierte so lange, bis die aus seiner Sicht optimale Lösung gefunden war.</p>
  </div>

  <div class="panel panel--construction">
    <div class="photo" role="img" aria-label="Nahaufnahme des gefrästen MDF-Profils mit Aluminiumschiene im Schnitt"></div>
  </div>

  <div class="panel panel--kitchen">
    <div class="photo photo--room" role="img" aria-label="Moderne weiße Küche mit Kochinsel und flächenbündig eingebauten Hochschränken"></div>
    <div class="photo photo--detail" role="img" aria-label="Detail der umlaufenden Lüftungsfuge am Schrank"></div>
    <svg class="frame-lines" viewBox="0 0 561 395" aria-hidden="true">
      <polyline points="255,27 515,27 515,185" fill="none" stroke="var(--frame)" stroke-width="2.5"/>
      <polyline points="40,95 40,320 365,320" fill="none" stroke="var(--frame)" stroke-width="2.5"/>
    </svg>
    <div class="brand">
      <span class="brand__mark"></span>
      <span class="brand__name">RAHMO 3.1 Entwurf<br>Jörg Wendtner</span>
    </div>
  </div>
</section>

<section class="spread spread--outside">
  <div class="panel panel--back-photo">
    <div class="photo" role="img" aria-label="Schrankkante mit aufgesetztem MDF-Profil vor dunklem Hintergrund"></div>
    <svg class="frame-lines" viewBox="0 0 199 400" aria-hidden="true">
      <polyline points="67,45 155,45 155,325" fill="none" stroke="var(--frame)" stroke-width="2.5"/>
      <polyline points="65,95 65,327 155,327" fill="none" stroke="var(--frame)" stroke-width="2.5"/>
    </svg>
  </div>

  <div class="panel panel--back">
    <address class="address">
      Talblick Küchen GmbH<br>
      Lindenweg 14<br>
      12345 Musterstadt<br>
      Tel: 01234 / 567890<br>
      Fax: 01234 / 567891<br>
      info@talblick-kuechen.de
    </address>
  </div>

  <div class="panel panel--cover">
    <h1 class="section-title">Lüftung als Designelement</h1>
    <div class="photo photo--portrait" role="img" aria-label="Schwarzweiß-Porträt des Erfinders in seiner Küchenausstellung"></div>
    <div class="brand">
      <span class="brand__mark"></span>
      <span class="brand__name">RAHMO 3.1 Entwurf<br>Jörg Wendtner</span>
    </div>
  </div>
</section>

</body>
</html>
```